Brightmoor Partners Branding Revamp

We are a consulting company, looking for a way to display and promote our brand. We have 2 sides to the business- Brightmoor (financial) and Partners (cyber security). The financial side products relate to business necessities: card processing, website design/hosting/maintenance, VoIP phone systems. The cyber security side promotes a bundled package of 4 solutions: network vulnerability scan, dark web scan, anti-ransomeware/malware software, and image-level backups. We want people to understand that partnering with Brightmoor Partners gives them “Elevated Peace of Mind” (tagline). Current badge and logos uploaded.

Target Market(s)

Small businesses

Contact Information for Business Card

Lena Marwick, Vice President, lena@brightmoorpartners.example, 555-806-1937, www.brightmoorpartners.example

Requirements
Nice to have
• I do prefer the darker background for front and back

```html
<!DOCTYPE html>
<html lang="en">
<head>
<meta charset="utf-8">
<title>Brightmoor Partners – Business Card</title>
<link rel="stylesheet" href="https://fonts.googleapis.com/css2?family=Montserrat:wght@500;600&family=Roboto:wght@300;400;700;900&display=swap">
<style>
  :root {
    --page: #ffffff;
    --card: #000000;
    --red: #e4202a;
    --red-deep: #8e0c12;
    --white: #ffffff;
    --shadow: rgba(0, 0, 0, 0.35);
  }
  * { margin: 0; padding: 0; box-sizing: border-box; }
  html, body {
    width: 731px;
    height: 1200px;
    overflow: hidden;
    background: var(--page);
  }
  .sheet {
    position: relative;
    width: 731px;
    height: 1200px;
  }
  .card {
    position: absolute;
    top: 320px;
    width: 320px;
    height: 559px;
    background: var(--card);
    overflow: hidden;
    box-shadow: 12px 14px 10px var(--shadow);
  }
  .card--back { left: 30px; }
  .card--front { left: 381px; }

  .brand {
    position: absolute;
    left: 0;
    width: 100%;
    text-align: center;
  }
  .brand__mark {
    display: block;
    width: 22px;
    height: 22px;
    margin: 0 auto 14px;
    background: var(--red);
  }
  .brand__name {
    font-family: "Montserrat", sans-serif;
    font-weight: 600;
    font-size: 19px;
    letter-spacing: 4px;
    text-transform: uppercase;
    color: var(--white);
    line-height: 1.35;
  }
  .card--back .brand { top: 238px; }
  .card--back .brand__name { font-size: 22px; }
  .card--front .brand { top: 138px; }

  .person {
    position: absolute;
    left: 30px;
    top: 286px;
    width: 262px;
  }
  .person__name {
    font-family: "Roboto", sans-serif;
    font-weight: 900;
    font-size: 28px;
    letter-spacing: -0.3px;
    color: var(--white);
    text-transform: uppercase;
    line-height: 1;
  }
  .person__role {
    display: flex;
    align-items: center;
    gap: 4px;
    margin-top: 4px;
  }
  .person__title {
    font-family: "Roboto", sans-serif;
    font-weight: 400;
    font-size: 12.5px;
    letter-spacing: 0.4px;
    color: var(--red);
    text-transform: uppercase;
    white-space: nowrap;
  }
  .person__rule {
    flex: 1;
    height: 10px;
    background: var(--red);
  }

  .contact {
    position: absolute;
    left: 30px;
    top: 360px;
    list-style: none;
  }
  .contact__item {
    display: flex;
    align-items: center;
    gap: 9px;
    height: 22.5px;
    font-family: "Roboto", sans-serif;
    font-weight: 300;
    font-size: 14px;
    color: var(--white);
    white-space: nowrap;
  }
  .contact__item:first-child { font-size: 17px; font-weight: 400; }
  .contact__icon { width: 14px; height: 14px; flex: none; }

  .accent {
    position: absolute;
  }
  .accent--top {
    left: 0;
    top: 0;
    width: 84px;
    height: 66px;
    background: linear-gradient(135deg, var(--red-deep), #3a0306 80%);
  }
  .accent--bottom {
    right: 0;
    bottom: 0;
    width: 150px;
    height: 125px;
    background: linear-gradient(135deg, var(--red), var(--red-deep));
  }
</style>
</head>
<body>
<main class="sheet">

  <section class="card card--back" aria-label="Card back">
    <div class="brand">
      <span class="brand__mark"></span>
      <p class="brand__name">Brightmoor<br>Partners</p>
    </div>
  </section>

  <section class="card card--front" aria-label="Card front">
    <div class="accent accent--top" role="img" aria-label="Angular red stripe decoration"></div>

    <div class="brand">
      <span class="brand__mark"></span>
      <p class="brand__name">Brightmoor Partners</p>
    </div>

    <div class="person">
      <h1 class="person__name">Lena Marwick</h1>
      <div class="person__role">
        <span class="person__title">Vice President</span>
        <span class="person__rule"></span>
      </div>
    </div>

    <ul class="contact">
      <li class="contact__item">
        <svg class="contact__icon" viewBox="0 0 16 16" aria-hidden="true">
          <circle cx="8" cy="8" r="8" fill="#fff"/>
          <path d="M5.2 3.8l1.4 1.6-.8 1.2c.6 1.3 1.6 2.3 2.9 2.9l1.2-.8 1.6 1.4-.9 1.5C7.8 11.4 4.6 8.2 3.8 4.7z" fill="#000"/>
        </svg>
        555-806-1937
      </li>
      <li class="contact__item">
        <svg class="contact__icon" viewBox="0 0 16 16" aria-hidden="true">
          <circle cx="8" cy="8" r="8" fill="#fff"/>
          <rect x="3.6" y="5" width="8.8" height="6" fill="none" stroke="#000" stroke-width="1.1"/>
          <path d="M3.6 5l4.4 3.4L12.4 5" fill="none" stroke="#000" stroke-width="1.1"/>
        </svg>
        lena@brightmoorpartners.example
      </li>
      <li class="contact__item">
        <svg class="contact__icon" viewBox="0 0 16 16" aria-hidden="true">
          <circle cx="8" cy="8" r="8" fill="#fff"/>
          <circle cx="8" cy="8" r="4.6" fill="none" stroke="#000" stroke-width="1"/>
          <ellipse cx="8" cy="8" rx="2" ry="4.6" fill="none" stroke="#000" stroke-width="1"/>
          <path d="M3.4 8h9.2" stroke="#000" stroke-width="1"/>
        </svg>
        www.brightmoorpartners.example
      </li>
    </ul>

    <div class="accent accent--bottom" role="img" aria-label="Angular red stripe decoration"></div>
  </section>

</main>
</body>
</html>
```